Bolt brace guard

We have created A revolutionary new design for door chains offering incredible strength and simplicity of instillation. Our product is called the Bolt Brace Guard. We are seeking a web site to promote and sell our lock. We want to promote that this lock is simple to install and much stronger than existing lock. www.boltbraceguards.com We are in the process of making a third video to replace the current one.. The first video is also on YouTube under toughest latch ever made early model test.

Target Market(s)

homeowners, apartments, dorm rooms, our someone wanting to turn a bedroom into a safe room ( somewhere they can go to in an emergency such as a break in).

Industry/Entity Type

Product

Font styles to use
Sans Serif

Requirements
Must have
• A video showing are product the weakness of existing door chains and the strength of are lock. A location where they can purchase our lock.
Nice to have
• A quick bio of the inventor of the lock a police officer for 22 years, retired but still concerned about safety and security

```html
<!DOCTYPE html>
<html lang="en">
<head>
<meta charset="utf-8">
<title>Bolt Brace Guards</title>
<link rel="stylesheet" href="https://fonts.googleapis.com/css2?family=Figtree:wght@400;500;600;700;800&display=swap">
<style>
:root{
  --blue:#1a73f0;
  --blue-dark:#0f5fd6;
  --ink:#111111;
  --text:#4a4a4a;
  --muted:#666666;
  --band:#f8f8f8;
  --rule:#e4e4e4;
  --arrow:#8a8a84;
  --white:#ffffff;
}
*{margin:0;padding:0;box-sizing:border-box}
html,body{width:966px;height:1200px;overflow:hidden;background:var(--white)}
body{font-family:"Figtree",Arial,sans-serif;color:var(--ink);position:relative}
a{text-decoration:none}
.page{position:relative;width:966px;height:1200px;border-top:2px solid #222;border-bottom:2px solid #222}

/* header */
.site-header{position:absolute;left:0;top:0;width:966px;height:80px;z-index:3}
.header-line{position:absolute;left:0;top:0;overflow:visible}
.nav{position:absolute;top:40px;font-size:9.5px;font-weight:500;letter-spacing:.2px;display:flex;align-items:center}
.nav a{color:var(--ink)}
.nav a.active{color:var(--blue)}
.nav .sep{margin:0 19px 0 18px;font-size:10px}
.nav-left{left:139px}
.nav-right{left:586px}
.phone{display:flex;align-items:center;gap:6px;font-weight:700;font-size:10.5px}
.brand{position:absolute;left:413px;top:22px;width:140px;height:90px;display:flex;flex-direction:column;align-items:center;justify-content:center;gap:6px}
.brand-dot{width:14px;height:14px;border-radius:50%;background:var(--blue)}
.brand-name{font-size:15px;font-weight:800;color:var(--blue);text-align:center;line-height:1.1;letter-spacing:.3px}

/* hero */
.hero{position:absolute;left:0;top:80px;width:966px;height:275px;overflow:hidden;z-index:1}
.hero-bg{position:absolute;inset:0;background:linear-gradient(180deg,#eef0f0 0%,#dfe5df 30%,#c9d6c0 45%,#e9ecea 62%,#f1f3f4 100%)}
.hero-photo{position:absolute;left:605px;top:0;width:361px;height:275px;background:linear-gradient(90deg,#f2f2f1 0%,#e7e6e3 40%,#d9d8d4 100%);border-left:3px solid #555}
.hero-title{position:absolute;left:140px;top:76px;font-size:24.5px;line-height:34px;letter-spacing:.6px;color:var(--ink);font-weight:400}
.hero-title strong{font-weight:800;font-size:27px;letter-spacing:.4px}
.btn{display:flex;align-items:center;justify-content:center;background:linear-gradient(180deg,#2a82f5,var(--blue-dark));color:var(--white);font-size:10px;font-weight:500}
.hero-btn{position:absolute;left:139px;top:183px;width:104px;height:32px}
.hero-link{position:absolute;left:258px;top:194px;font-size:11px;color:var(--white);letter-spacing:.3px}
.slide-arrow{position:absolute;top:110px;width:36px;height:56px;background:var(--arrow);display:flex;align-items:center;justify-content:center}
.slide-arrow.prev{left:0}
.slide-arrow.next{right:0}
.dots{position:absolute;left:470px;top:257px;display:flex;gap:3px}
.dots span{width:6px;height:6px;border-radius:50%;background:#c9ccd0}
.dots span.on{background:#6d6f73}

/* welcome */
.welcome-title{position:absolute;left:141px;top:394px;font-size:26px;font-weight:400;letter-spacing:.5px}
.welcome-sub{position:absolute;left:141px;top:434px;font-size:13px;font-weight:700;color:var(--blue);letter-spacing:.3px}
.welcome-text{position:absolute;left:140px;top:456px;width:305px;font-size:11.5px;line-height:14px;color:var(--text)}
.welcome-btn{position:absolute;left:138px;top:534px;width:97px;height:29px}
.video{position:absolute;left:496px;top:394px;width:332px;height:175px;background:linear-gradient(90deg,#d4d4d2 0%,#e5e4e2 35%,#cfcecb 70%,#bdbcb8 100%);border:1px solid #d0d0d0}
.play{position:absolute;left:135px;top:57px}

/* benefits */
.benefits{position:absolute;left:0;top:616px;width:966px;height:216px;background:var(--band);border-top:1px solid var(--rule);border-bottom:1px solid var(--rule)}
.benefits-title{position:absolute;left:0;width:966px;top:24px;text-align:center;font-size:25px;font-weight:800;color:var(--blue);letter-spacing:.5px}
.benefits-lede{position:absolute;left:0;width:966px;top:57px;text-align:center;font-size:12.5px;color:var(--ink)}
.benefit{position:absolute;top:106px;width:100px;text-align:center;font-size:10px;font-weight:600;letter-spacing:.3px}
.benefit svg{display:block;margin:0 auto 16px}

/* testimonial */
.portrait{position:absolute;left:138px;top:868px;width:89px;height:106px;background:linear-gradient(180deg,#2b4270 0%,#3b5480 45%,#a89770 100%)}
.person-name{position:absolute;left:120px;width:125px;top:983px;text-align:center;font-size:10.5px;font-weight:700;color:var(--blue)}
.person-role{position:absolute;left:120px;width:125px;top:999px;text-align:center;font-size:9.5px;color:var(--muted);font-weight:500}
.quote-mark{position:absolute;font-size:18px;font-weight:800;color:#555;line-height:1}
.quote{position:absolute;left:251px;top:884px;width:206px;font-size:8px;line-height:11.1px;color:#444}
.chain-photo{position:absolute;left:494px;top:857px;width:334px;height:162px;background:linear-gradient(90deg,#d8d6d0 0%,#cfc9b9 35%,#c2b79a 60%,#d6d4cf 100%)}

/* purchase band */
.buy{position:absolute;left:0;top:1049px;width:966px;height:84px;background:var(--band);border-top:1px solid var(--rule);border-bottom:1px solid var(--rule)}
.buy-pin{position:absolute;left:142px;top:18px}
.buy-q{position:absolute;left:183px;top:23px;font-size:11.5px;letter-spacing:.3px}
.buy-q em{font-style:normal;color:var(--blue)}
.buy-address{position:absolute;left:182px;top:37px;font-size:21px;color:var(--blue);letter-spacing:.3px}
.buy-btn{position:absolute;left:617px;top:18px;width:211px;height:45px;font-size:11.5px;letter-spacing:.3px}

/* footer */
.copyright{position:absolute;left:140px;top:1157px;font-size:9.5px;color:#333}
.social{position:absolute;left:703px;top:1152px;display:flex;gap:12px}
.social span{width:23px;height:23px;border-radius:50%;background:var(--blue)}
</style>
</head>
<body>
<div class="page">

  <header class="site-header">
    <svg class="header-line" width="966" height="122" viewBox="0 0 966 122">
      <path d="M402 79 C410 104 440 118 483 118 C526 118 556 104 564 79 Z" fill="#ffffff"/>
      <path d="M0 80 H402 C410 104 440 118 483 118 C526 118 556 104 564 80 H966" fill="none" stroke="#1a73f0" stroke-width="1.5"/>
    </svg>
    <nav class="nav nav-left">
      <a class="active" href="#">HOME</a><span class="sep">/</span>
      <a href="#">ABOUT</a><span class="sep">/</span>
      <a href="#">PRODUCTS</a><span class="sep">/</span>
      <a href="#">BLOG</a>
    </nav>
    <div class="brand">
      <span class="brand-dot"></span>
      <span class="brand-name">BOLT BRACE<br>GUARDS</span>
    </div>
    <nav class="nav nav-right">
      <a href="#">NEWS</a><span class="sep">/</span>
      <a href="#">CONTACT</a><span class="sep">/</span>
      <span class="phone">
        <svg width="12" height="12" viewBox="0 0 24 24"><path d="M6.6 10.8a15 15 0 0 0 6.6 6.6l2.2-2.2c.3-.3.7-.4 1-.2 1.1.4 2.3.6 3.6.6.6 0 1 .4 1 1V20c0 .6-.4 1-1 1A17 17 0 0 1 3 4c0-.6.4-1 1-1h3.5c.6 0 1 .4 1 1 0 1.3.2 2.5.6 3.6.1.3 0 .7-.2 1z" fill="#1a73f0"/></svg>
        0800 (555) 0199
      </span>
    </nav>
  </header>

  <section class="hero">
    <div class="hero-bg" role="img" aria-label="Blurred garden and window backdrop"></div>
    <div class="hero-photo" role="img" aria-label="Door with a gold handle fitted with the door chain guard"></div>
    <h1 class="hero-title">WE PROVIDE THE ULTIMATE<br><strong>SECURITY AND SAFETY</strong><br>FOR YOUR FAMILY !</h1>
    <a class="btn hero-btn" href="#">Read More</a>
    <span class="hero-link">Watch A Video !</span>
    <div class="slide-arrow prev"><svg width="12" height="20" viewBox="0 0 12 20"><path d="M10 2 2 10l8 8" fill="none" stroke="#fff" stroke-width="1.6"/></svg></div>
    <div class="slide-arrow next"><svg width="12" height="20" viewBox="0 0 12 20"><path d="M2 2l8 8-8 8" fill="none" stroke="#fff" stroke-width="1.6"/></svg></div>
    <div class="dots"><span class="on"></span><span></span><span></span></div>
  </section>

  <h2 class="welcome-title">WELCOME !</h2>
  <p class="welcome-sub">WATCH A VIDEO...</p>
  <p class="welcome-text">“Bolt brace guard “We havethe strongest, simplest and most versatile door chain on the market, Period. We provide a ultimate security and safety for your family. There is nothing else on the market equal to bolt brace guard.</p>
  <a class="btn welcome-btn" href="#">Read More</a>
  <div class="video" role="img" aria-label="Video still of a door handle with the chain guard fitted">
    <svg class="play" width="62" height="62" viewBox="0 0 62 62">
      <circle cx="31" cy="31" r="29" fill="#222" stroke="#fff" stroke-width="3"/>
      <path d="M24 18v26l21-13z" fill="#fff"/>
    </svg>
  </div>

  <section class="benefits">
    <h2 class="benefits-title">BENEFITS !</h2>
    <p class="benefits-lede">Six &nbsp;Reasons the <strong>bolt brace guard</strong> is better than existing door chains...</p>

    <div class="benefit" style="left:119px">
      <svg width="40" height="46" viewBox="0 0 40 46"><path d="M20 2 37 8v13c0 12-8 19-17 23C11 40 3 33 3 21V8z" fill="none" stroke="#1a73f0" stroke-width="3"/><path d="M12 30 28 12M14 36l16-18" stroke="#1a73f0" stroke-width="3"/></svg>SECURITY</div>
    <div class="benefit" style="left:248px">
      <svg width="40" height="46" viewBox="0 0 40 46"><path d="M11 20v-7a9 9 0 0 1 18 0v7" fill="none" stroke="#1a73f0" stroke-width="4"/><rect x="3" y="20" width="34" height="24" rx="3" fill="#1a73f0"/><circle cx="20" cy="30" r="3" fill="#fff"/><rect x="18.5" y="31" width="3" height="7" fill="#fff"/></svg>STRONGER</div>
    <div class="benefit" style="left:373px">
      <svg width="46" height="46" viewBox="0 0 46 46"><rect x="4" y="20" width="26" height="12" rx="6" transform="rotate(-45 17 26)" fill="none" stroke="#1a73f0" stroke-width="5"/><rect x="16" y="14" width="26" height="12" rx="6" transform="rotate(-45 29 20)" fill="none" stroke="#1a73f0" stroke-width="5"/></svg>SIMPLER</div>
    <div class="benefit" style="left:494px">
      <svg width="52" height="46" viewBox="0 0 52 46"><path d="M8 40a22 22 0 1 1 36 0" fill="none" stroke="#1a73f0" stroke-width="5"/><path d="M26 28 22 8" stroke="#1a73f0" stroke-width="3"/><rect x="20" y="36" width="12" height="6" fill="#1a73f0"/></svg>SPEEDIER</div>
    <div class="benefit" style="left:624px">
      <svg width="46" height="46" viewBox="0 0 46 46"><g stroke="#1a73f0" stroke-width="1.6"><path d="M22 24 38 8M22 24 6 20M22 24 10 40M22 24 34 40M22 24 20 4"/></g><g fill="#1a73f0"><circle cx="22" cy="24" r="4"/><circle cx="38" cy="8" r="3.5"/><circle cx="6" cy="20" r="3"/><circle cx="10" cy="40" r="3.5"/><circle cx="34" cy="40" r="3"/><circle cx="20" cy="4" r="2.5"/></g></svg>STRUCTURE</div>
    <div class="benefit" style="left:750px">
      <svg width="46" height="46" viewBox="0 0 46 46"><rect x="2" y="20" width="9" height="24" fill="#1a73f0"/><path d="M14 21 24 6c2-3 6-2 6 2l-2 10h12c3 0 5 3 4 6l-4 16c-1 3-3 4-5 4H14z" fill="#1a73f0"/></svg>USE</div>
  </section>

  <div class="portrait" role="img" aria-label="Portrait of the inventor, a retired police captain in uniform"></div>
  <p class="person-name">DANIEL MORROW</p>
  <p class="person-role">CAPTAIN</p>
  <span class="quote-mark" style="left:236px;top:872px">“</span>
  <p class="quote">Lorem ipsum dolor sit amet, consectetuer adipiscing elit, sed diam nonummy nibh euismod tincidunt ut laoreet dolore magna aliquam erat volutpat. Ut wisi enim ad minim veniam, quis nostrud exerci tation ullamcorper suscipit lobortis nisl ut aliquip ex ea commodo consequat. Duis autem vel eum iriure dolor in hendrerit in vulputate olore te feugait nulla facilisi</p>
  <span class="quote-mark" style="left:456px;top:955px">”</span>
  <div class="chain-photo" role="img" aria-label="Close-up of the brass door chain guard with hinge plate and ring"></div>

  <section class="buy">
    <svg class="buy-pin" width="30" height="46" viewBox="0 0 30 46"><path d="M15 1C7 1 1 7 1 15c0 10 14 30 14 30s14-20 14-30C29 7 23 1 15 1z" fill="#1a73f0"/><circle cx="15" cy="15" r="7" fill="none" stroke="#fff" stroke-width="3"/></svg>
    <p class="buy-q">WANT YOU BUY THIS <em>AMAZING</em> DOOR CHAIN LOCK ?</p>
    <p class="buy-address">134,Lorem ipsum dolor sit amet.</p>
    <a class="btn buy-btn" href="#">CONTACT US NOW</a>
  </section>

  <footer>
    <p class="copyright">Copyright © 2014. BOLT BRACE GUARDS Inc. &nbsp;All Right Reserved.</p>
    <div class="social"><span></span><span></span><span></span><span></span></div>
  </footer>

</div>
</body>
</html>
```